Ridgeway Provisioning Group needs a cool web design

We need a web design for a new start up called Ridgeway Provisioning Group. RPG is all about working with mine sites to reduce costs and make their supply chains more effective and cost efficient. I have attached our logo and a very basic tile format layout for the website but I will take your advice on best layout. I do prefer a tile based page similar to "Varnholt.com/advisory" this displays a professional yet cool look. The secondary pages need to have the same format.
Target Market(s)
Target customers are typically men in the mining industry. They want simplicity and are time poor.
Industry/Entity Type
Mining
Coding
Coded - Design and coding required
Requirements
Must have
- Must be simple, prefer tile based such as the Varnholts.com/advisory website.
Use bold writing and fonts. No flowery fonts.
Must use corporate colors but don't make too dark.
the site must have connections to well designed second pages.

```html
<!DOCTYPE html>
<html lang="en">
<head>
<meta charset="utf-8">
<title>Ridgeway Provisioning Group</title>
<link rel="stylesheet" href="https://fonts.googleapis.com/css2?family=Aldrich&family=Montserrat:wght@300;400&family=Open+Sans:wght@400&display=swap">
<style>
  :root {
    --header-dark: #262626;
    --header-mid: #333333;
    --brand-red: #b3121a;
    --tile-red: #a8121a;
    --page-bg: #f2f2f2;
    --tile-bg: #efefef;
    --tile-edge: #5e5e5e;
    --text-dark: #3a3a3a;
    --heading: #1a1a1a;
    --white: #ffffff;
    --footer-rule: #111111;
  }
  * { box-sizing: border-box; margin: 0; padding: 0; }
  html, body { width: 1200px; height: 918px; overflow: hidden; }
  body {
    position: relative;
    background: var(--page-bg);
    font-family: "Montserrat", Arial, sans-serif;
  }
  .site-header {
    position: absolute; left: 0; top: 0; width: 1200px; height: 140px;
    background: linear-gradient(180deg, var(--header-mid), var(--header-dark));
    border-bottom: 5px solid var(--brand-red);
    height: 145px;
  }
  .brand {
    position: absolute; left: 136px; top: 20px;
    display: flex; align-items: center; gap: 18px;
  }
  .brand-square { width: 40px; height: 40px; background: var(--brand-red); }
  .brand-name {
    font-family: "Aldrich", Arial, sans-serif;
    color: var(--white); font-size: 25px; line-height: 34px;
    text-transform: uppercase; letter-spacing: 1px;
  }
  .main-nav {
    position: absolute; right: 140px; top: 119px;
    display: flex; gap: 20px;
  }
  .main-nav a {
    color: var(--white); text-decoration: none; font-size: 13px; font-family: "Montserrat", Arial, sans-serif;
  }
  .tile {
    position: absolute;
    display: flex; align-items: center; justify-content: center; text-align: center;
    background: linear-gradient(180deg, #f5f5f5, #e9e9e9);
    border: 1px solid #dcdcdc;
    border-bottom: 3px solid var(--tile-edge);
    border-radius: 2px;
    box-shadow: 0 1px 2px rgba(0,0,0,0.15);
    font-family: "Aldrich", Arial, sans-serif;
    color: var(--tile-red); font-size: 17px; line-height: 22px; letter-spacing: 1px;
    text-decoration: none;
  }
  .service-tile { left: 136px; width: 175px; height: 91px; }
  .hero {
    position: absolute; left: 322px; top: 145px; width: 742px; height: 282px;
    background: linear-gradient(90deg, #6f6b66 0%, #8f8a83 35%, #d8d6d2 60%, #9d9fa5 80%, #c9c2bb 100%);
  }
  .welcome { position: absolute; left: 330px; top: 433px; width: 726px; }
  .welcome h1 {
    font-family: "Open Sans", Arial, sans-serif; font-weight: 400;
    font-size: 29px; color: var(--heading); line-height: 38px;
  }
  .welcome p {
    margin-top: 6px; font-size: 13.4px; line-height: 21.8px; color: var(--text-dark);
    font-weight: 400;
  }
  .site-footer {
    position: absolute; left: 0; top: 776px; width: 1200px; height: 142px;
    border-top: 5px solid var(--footer-rule);
  }
  .footer-backdrop {
    position: absolute; inset: 0;
    background: linear-gradient(180deg, #bfb8ac 0%, #cfc8bb 40%, #b9ae96 75%, #c7c0b2 100%);
  }
  .footer-nav {
    position: absolute; left: 0; right: 0; top: 18px;
    display: flex; justify-content: center; align-items: center; gap: 12px;
    font-size: 13px; color: var(--heading);
  }
  .footer-nav a { color: var(--heading); text-decoration: none; }
  .footer-nav .divider { font-size: 9px; }
  .copyright {
    position: absolute; left: 0; right: 0; top: 119px; text-align: center;
    font-size: 10.5px; color: var(--heading); letter-spacing: 0.3px;
  }
</style>
</head>
<body>
  <header class="site-header">
    <div class="brand">
      <span class="brand-square"></span>
      <span class="brand-name">Ridgeway<br>Provisioning<br>Group</span>
    </div>
    <nav class="main-nav">
      <a href="#">HOME</a>
      <a href="#">CONTACT US</a>
    </nav>
  </header>

  <a class="tile service-tile" href="#" style="top:155px">Procurement<br>Services</a>
  <a class="tile service-tile" href="#" style="top:257px">Strategic<br>Sourcing<br>Services</a>
  <a class="tile service-tile" href="#" style="top:360px">Lead Time<br>Reduction<br>Services</a>
  <a class="tile service-tile" href="#" style="top:462px">Inventory<br>Optimisation<br>Services</a>
  <a class="tile service-tile" href="#" style="top:564px">Critical Spare<br>Parts Audit</a>
  <a class="tile service-tile" href="#" style="top:667px">Supply Chain<br>Health Check</a>

  <div class="hero" role="img" aria-label="Excavator loading a haul truck at a mine site beside a team of business professionals reviewing plans"></div>

  <section class="welcome">
    <h1>Welcome to Ridgeway Provisioning Group</h1>
    <p>This is Photoshop's version&nbsp; of Lorem Ipsum. Proin gravida nibh vel velit auctor aliquet. Aenean sollicit iou, lorem quis bibendum auctor, nisi elit consequat ipsum, nec sagittis sem nibh id elit. Duis sed odio sit amei opt nibh vulputate cursus a sit amet mauris. Morbi accumsan ipsum velit. Nam nec tellus a odio tincidunto auctoro a ornare odio. Sed non&nbsp; mauris vitae erat consequat auctor eu in elit. Class aptent taciti sociosqui ad litor kwe a torquent per conubia nostra, per inceptos himenaeos. Mauris in erat justo. Nullam ac urnadi eu felis dapib ius condimentum sit amet a augue. Sed non neque elit. Sed ut imperdiet nisi. Proin conuiok dimentum fermentum ok nunc. Etiam pharetra, erat sed fermentum feugiat, velit mauris egestas quam.</p>
  </section>

  <a class="tile" href="#" style="left:322px; top:667px; width:360px; height:91px">Case Studies</a>
  <a class="tile" href="#" style="left:700px; top:667px; width:361px; height:91px">Global Presence</a>

  <footer class="site-footer">
    <div class="footer-backdrop" role="img" aria-label="Blurred view of terraced open-pit mine with machinery"></div>
    <nav class="footer-nav">
      <a href="#">Home</a><span class="divider">|</span><a href="#">Contact Us</a>
    </nav>
    <p class="copyright">Copyright © 2015 Ridgeway Provisioning Group, All rights reserved</p>
  </footer>
</body>
</html>
```